professional business card

A Clean looking business card for a money transfer company. Our company is call Velorix= Transfer + Send = Transcend (next level)
to show professionalism as well as some effects to show digital tech.

1 side to have position, name and address
2 side to have company name and show that we provide money exchange and cross-border money transfer

Target Market(s)

Remittance companies and high net worth individuals

Industry/Entity Type

Finance

Contact Information for Business Card

Name, address, email, title, services- money exchange and cross-border remittance

Requirements
Nice to have
• Digital age feel

```html
<!DOCTYPE html>
<html lang="en">
<head>
<meta charset="utf-8">
<title>Velorix business card</title>
<link rel="stylesheet" href="https://fonts.googleapis.com/css2?family=Source+Sans+3:wght@400;600;700&display=swap">
<style>
  :root {
    --backdrop: #e3e4e6;
    --navy: #13283a;
    --teal: #6cc4d3;
    --white: #ffffff;
    --ink: #13283a;
    --muted: #5d6b78;
    --divider: rgba(255,255,255,0.08);
  }
  html, body {
    margin: 0;
    padding: 0;
    width: 1200px;
    height: 803px;
    overflow: hidden;
    background: var(--backdrop);
    font-family: "Source Sans 3", "Segoe UI", sans-serif;
  }
  .stage {
    position: relative;
    width: 1200px;
    height: 803px;
  }
  .card {
    position: absolute;
    top: 258px;
    width: 500px;
    height: 286px;
    box-sizing: border-box;
    overflow: hidden;
    box-shadow: 0 10px 24px rgba(0,0,0,0.18);
  }
  .card--front {
    left: 70px;
    background: var(--navy);
    color: var(--white);
  }
  .card--back {
    left: 630px;
    background: var(--white);
  }
  .tech-lines {
    position: absolute;
    pointer-events: none;
  }
  .tech-lines--front {
    right: 0;
    top: 0;
    width: 200px;
    height: 80px;
  }
  .tech-lines--back {
    left: 0;
    bottom: 0;
    width: 180px;
    height: 70px;
  }
  .brand-mark {
    position: absolute;
    left: 48px;
    top: 124px;
    display: flex;
    align-items: center;
    gap: 8px;
    color: var(--teal);
    font-weight: 700;
    font-size: 26px;
    letter-spacing: 1px;
  }
  .brand-dot {
    width: 14px;
    height: 14px;
    border-radius: 50%;
    background: var(--teal);
  }
  .divider {
    position: absolute;
    left: 222px;
    top: 0;
    width: 1px;
    height: 82px;
    background: var(--divider);
  }
  .contact {
    position: absolute;
    left: 236px;
    top: 88px;
  }
  .contact__name {
    margin: 0;
    color: var(--teal);
    font-weight: 700;
    font-size: 17px;
    letter-spacing: 0.5px;
    text-transform: uppercase;
  }
  .contact__title {
    margin: 0 0 10px;
    font-size: 13px;
    font-weight: 400;
  }
  .contact__list {
    list-style: none;
    margin: 0;
    padding: 0;
  }
  .contact__item {
    display: flex;
    align-items: center;
    gap: 8px;
    font-size: 12.5px;
    line-height: 20px;
  }
  .contact__icon {
    width: 12px;
    height: 12px;
    flex: none;
  }
  .back-content {
    position: absolute;
    inset: 0;
    display: flex;
    flex-direction: column;
    align-items: center;
    justify-content: center;
    gap: 10px;
  }
  .wordmark {
    display: flex;
    align-items: center;
    gap: 12px;
    color: var(--ink);
    font-weight: 700;
    font-size: 40px;
    letter-spacing: 1px;
    text-transform: uppercase;
  }
  .wordmark__dot {
    width: 22px;
    height: 22px;
    border-radius: 50%;
    background: var(--teal);
  }
  .services {
    margin: 0;
    color: var(--muted);
    font-size: 12px;
    font-weight: 600;
    letter-spacing: 2px;
    text-transform: uppercase;
  }
  .services__sep {
    color: var(--teal);
    padding: 0 6px;
  }
</style>
</head>
<body>
<main class="stage">
  <section class="card card--front" aria-label="Card front with contact details">
    <svg class="tech-lines tech-lines--front" viewBox="0 0 200 80" aria-hidden="true">
      <g fill="none" stroke="var(--teal)" stroke-width="1" opacity="0.28">
        <path d="M200 18 H150 L136 32 H100"/>
        <path d="M200 40 H168 L154 54 H128"/>
        <path d="M200 62 H180"/>
      </g>
      <g fill="var(--teal)" opacity="0.4">
        <circle cx="100" cy="32" r="2.5"/>
        <circle cx="128" cy="54" r="2.5"/>
        <circle cx="180" cy="62" r="2.5"/>
      </g>
    </svg>
    <div class="brand-mark"><span class="brand-dot"></span>Velorix</div>
    <div class="divider"></div>
    <div class="contact">
      <h1 class="contact__name">Daniel Reyes</h1>
      <p class="contact__title">Manager</p>
      <ul class="contact__list">
        <li class="contact__item">
          <svg class="contact__icon" viewBox="0 0 12 12" aria-hidden="true">
            <circle cx="6" cy="6" r="6" fill="var(--teal)"/>
            <path d="M4 3.2 L5 3 L5.6 4.6 L5 5.1 Q5.6 6.4 6.9 7 L7.4 6.4 L9 7 L8.8 8 Q6.5 8.6 4.6 6.6 Q3.2 4.9 4 3.2Z" fill="var(--navy)"/>
          </svg>
          415-802-6271
        </li>
        <li class="contact__item">
          <svg class="contact__icon" viewBox="0 0 12 12" aria-hidden="true">
            <circle cx="6" cy="6" r="6" fill="var(--teal)"/>
            <rect x="3" y="4" width="6" height="4.2" fill="none" stroke="var(--navy)" stroke-width="0.9"/>
            <path d="M3 4 L6 6.4 L9 4" fill="none" stroke="var(--navy)" stroke-width="0.9"/>
          </svg>
          info@velorix.com
        </li>
        <li class="contact__item">
          <svg class="contact__icon" viewBox="0 0 12 12" aria-hidden="true">
            <circle cx="6" cy="6" r="6" fill="var(--teal)"/>
            <circle cx="6" cy="6" r="3" fill="none" stroke="var(--navy)" stroke-width="0.9"/>
            <path d="M3 6 H9 M6 3 Q4.4 6 6 9 M6 3 Q7.6 6 6 9" fill="none" stroke="var(--navy)" stroke-width="0.8"/>
          </svg>
          www.velorix.com
        </li>
        <li class="contact__item">
          <svg class="contact__icon" viewBox="0 0 12 12" aria-hidden="true">
            <circle cx="6" cy="6" r="6" fill="var(--teal)"/>
            <path d="M6 9.4 Q3.6 6.6 3.6 5 A2.4 2.4 0 0 1 8.4 5 Q8.4 6.6 6 9.4Z" fill="var(--navy)"/>
            <circle cx="6" cy="5" r="0.9" fill="var(--teal)"/>
          </svg>
          2840, Harbor Lane 9, Oakland, CA 94607
        </li>
      </ul>
    </div>
  </section>

  <section class="card card--back" aria-label="Card back with company name and services">
    <svg class="tech-lines tech-lines--back" viewBox="0 0 180 70" aria-hidden="true">
      <g fill="none" stroke="var(--teal)" stroke-width="1" opacity="0.35">
        <path d="M0 20 H40 L54 34 H90"/>
        <path d="M0 44 H24 L38 58 H70"/>
      </g>
      <g fill="var(--teal)" opacity="0.5">
        <circle cx="90" cy="34" r="2.5"/>
        <circle cx="70" cy="58" r="2.5"/>
      </g>
    </svg>
    <div class="back-content">
      <div class="wordmark"><span class="wordmark__dot"></span>Velorix</div>
      <p class="services">Money Exchange<span class="services__sep">|</span>Cross-Border Remittance</p>
    </div>
  </section>
</main>
</body>
</html>
```